Design eines Zertifikats
Ich bin total begeistert. Super Kommunikation, super schnelle Reaktion auf kleine Änderungswünsche, ich bin wirklich rundum zufrieden!! Auch bei weiterführenden Fragen die gar nicht direkt mit dem Design zusammenhingen wurde mir total schnell und sympathisch geholfen, ich kann die Designerin nur wärmstens weiterempfehlen!
Zielgruppe
Ich betreibe einen Onlineshop, in dem ich sogenannte Sterntaufen verkaufe. Ein Kunde bekommt dabei im Zuge seines Kaufes ein Zertifikat ausgestellt mit Daten zu seinem getauften Stern. Es geht hier um das Design eines neuen Zertifikats um möglichst noch mehr Käufer anzusprechen. Es sind bereits 3 Designs vorhanden, das neue sollte sich entsprechend etwas absetzen.
Ich lasse die Zertifikate in einer Druckerei drucken, und bedrucke diese dann selber mit den Daten der Sterntaufe, es muss auf dem Zertifikat also ein heller Bereich vorhanden sein in dem ich drucken kann.
Aufgabenstellung
Das Zertifikat soll A4 sein. Es sollte modern sein und sich wie gesagt möglichst von den bestehenden absetzen, und ein möglichst breites Publikum ansprechen.
Beispiele für Zertifikate der Konkurrenz finden sich unter:
lichtpunkt-shop.de
nebelbuchung.de
himmelsgabe-online.de
Das von lichtpunkt-shop.de gefällt mir persönlich ganz gut, aber lasst euch nicht von den Vorschlägen einschränken.
Bitte nicht zu exzessiv kostenpflichtiges Stockmaterial verwenden, ich mache leider aktuell noch Miese mit dem Shop :-)
Bitte schaut auf meine Webseite um ein Gefühl dafür zu bekommen wie viel Platz für Text vorhanden sein muss.

```html
<!DOCTYPE html>
<html lang="de">
<head>
<meta charset="utf-8">
<title>Himmelsbrief – Zertifikat</title>
<link href="https://fonts.googleapis.com/css2?family=Poppins:wght@400;600;700&display=swap" rel="stylesheet">
<style>
  :root {
    --night-top: #1c1b4f;
    --night-bottom: #33327a;
    --gold-light: #f0d98c;
    --gold: #d6b15a;
    --gold-dark: #c99a3c;
    --paper: #f4f5f6;
    --ink: #111111;
    --white: #ffffff;
  }
  * { margin: 0; padding: 0; box-sizing: border-box; }
  html, body { width: 1200px; height: 849px; overflow: hidden; }
  body { font-family: "Poppins", sans-serif; color: var(--ink); background: var(--paper); }
  .certificate { position: relative; width: 1200px; height: 849px; overflow: hidden; }
  .backdrop { position: absolute; inset: 0; }
  .brand {
    position: absolute; left: 0; top: 118px; width: 1200px;
    text-align: center;
  }
  .brand-name {
    font-weight: 400; font-size: 38px; line-height: 1;
    letter-spacing: 10px; text-transform: uppercase;
    color: var(--white);
  }
  .frame {
    position: absolute; left: 43px; top: 410px; width: 1114px; height: 418px;
    border: 4px solid var(--gold); border-top: none;
  }
  .details { position: absolute; left: 0; top: 384px; width: 1200px; text-align: center; }
  .heading { font-weight: 600; font-size: 19px; line-height: 1; }
  .data-table {
    display: grid; grid-template-columns: 606px 1fr; column-gap: 38px; row-gap: 9px;
    font-size: 17px; line-height: 18px; text-align: left; margin-top: 42px;
  }
  .data-table dt { text-align: right; }
  .heading-baptised { margin-top: 42px; }
  .star-name { font-weight: 700; font-size: 36px; letter-spacing: 4px; margin-top: 30px; line-height: 1; }
  .data-table.registration { margin-top: 34px; }
</style>
</head>
<body>
<main class="certificate">
  <svg class="backdrop" width="1200" height="849" viewBox="0 0 1200 849">
    <defs>
      <linearGradient id="night" x1="0" y1="0" x2="0" y2="1">
        <stop offset="0" stop-color="#1c1b4f"/>
        <stop offset="1" stop-color="#33327a"/>
      </linearGradient>
      <linearGradient id="goldBand" x1="0" y1="0" x2="1" y2="0">
        <stop offset="0" stop-color="#f0d98c"/>
        <stop offset="0.5" stop-color="#c99a3c"/>
        <stop offset="1" stop-color="#f0d98c"/>
      </linearGradient>
    </defs>
    <rect class="night-sky" x="0" y="0" width="1200" height="400" fill="url(#night)" role="img" aria-label="Sternenhimmel mit Sternbildlinien"/>
    <path class="gold-arc" d="M0,328 Q600,242 1200,328 L1200,420 L0,420 Z" fill="url(#goldBand)"/>
    <path class="paper" d="M0,388 Q600,210 1200,388 L1200,849 L0,849 Z" fill="#f4f5f6"/>
  </svg>

  <header class="brand">
    <div class="brand-name">Himmelsbrief</div>
  </header>

  <div class="frame"></div>

  <section class="details">
    <h2 class="heading">Der Stern mit den Daten</h2>
    <dl class="data-table">
      <dt>HIP-No.</dt><dd>11767</dd>
      <dt>Rektamension</dt><dd>02h 31m 47.08s</dd>
      <dt>Deklination</dt><dd>+89° 15' 50.9"</dd>
      <dt>Scheinbare Magnitude</dt><dd>1,97</dd>
    </dl>
    <h2 class="heading heading-baptised">wurde auf der Namen getauft</h2>
    <p class="star-name">Maria</p>
    <dl class="data-table registration">
      <dt>Taufdatum</dt><dd>14.02.2020</dd>
      <dt>Registrationsnummer</dt><dd>xxx-xxx-xxx-xxx</dd>
    </dl>
  </section>
</main>
</body>
</html>
```